Business card for wedding & event planning company

I'm looking for a well designed double sided business card to represent my wedding and event planning company.

It should include the fact we manage the following events:
Weddings, birthdays, conferences, product launches, fashion shows & conventions
in the following areas:
Wiltshire, Oxfordshire, Berkshire & London

My contact details to be included are:

Moira Lintell
07741 308562
moira@amberfinchgatherings.co.uk
www.amberfinchgatherings.co.uk

My logo can be found at the following Filevaultly location:
AI file: https://www.filevaultly.com/s/k3mprt8wq51bn2x/brief_480317_2290451_7735102_sourcefile.ai?dl=0
PNG file:
https://www.filevaultly.com/s/hv7ncqeyb4tlofu/brief_480317_2290451_7735102_e8a1b406_image.png?dl=0

Target Market(s)

women aged 30-55

Industry/Entity Type

Wedding

Contact Information for Business Card

in the following areas:

Moira Lintell
Event Planner
07741 308562

Font styles to use
Serif
Sans Serif
Script

Requirements
Must have
• Purple and white colour scheme
Should not have
• Black background
• Please don't submit any of the see-through business card designs.

```html
<!DOCTYPE html>
<html lang="en">
<head>
<meta charset="utf-8">
<title>Ashcombe &amp; Vale – Business Card</title>
<link rel="stylesheet" href="https://fonts.googleapis.com/css2?family=Cinzel:wght@400;600&family=Cormorant+Garamond:wght@500&display=swap">
<style>
  :root {
    --stage: #2b2b2b;
    --card: #ffffff;
    --purple: #8a2f93;
    --ink: #333333;
    --rule: #555555;
    --hairline: #d4d4d4;
    --ornament: #d9d4da;
  }
  * { margin: 0; padding: 0; box-sizing: border-box; }
  html, body { width: 1200px; height: 933px; overflow: hidden; }
  body { background: var(--stage); position: relative; font-family: "Cinzel", serif; }

  .card {
    position: absolute; left: 338px; width: 525px; height: 300px;
    background: var(--card); border-radius: 22px; overflow: hidden;
  }
  .card--front { top: 130px; }
  .card--back { top: 507px; }

  /* Front */
  .brand-name {
    position: absolute; left: 338px; width: 525px; top: 238px;
    text-align: center; color: var(--purple); font-size: 38px; font-weight: 400; line-height: 1;
  }
  .brand-rule {
    position: absolute; left: 482px; width: 236px; top: 300px; height: 1px; background: var(--hairline);
  }
  .services { position: absolute; top: 330px; list-style: none; color: var(--ink); font-size: 13.5px; line-height: 15px; }
  .services li::before { content: "· "; }
  .services--a { left: 414px; }
  .services--b { left: 511px; }
  .services--c { left: 671px; }

  .divider { position: absolute; left: 413px; width: 375px; height: 10px; }
  .divider--front { top: 368px; }
  .divider--back { top: 745px; }

  .areas-label {
    position: absolute; left: 338px; width: 525px; top: 386px; text-align: center;
    color: var(--purple); font-size: 10px; letter-spacing: 4.5px;
  }
  .areas {
    position: absolute; left: 338px; width: 525px; top: 396px; text-align: center;
    color: var(--purple); font-size: 14px; letter-spacing: 0.8px;
  }

  /* Back */
  .flourish {
    position: absolute; left: 388px; top: 552px; width: 400px; height: 52px;
    background: linear-gradient(180deg, #f4f2f4 0%, var(--ornament) 100%); border-radius: 4px;
  }
  .person {
    position: absolute; left: 338px; width: 525px; top: 620px; text-align: center;
    font-family: "Cormorant Garamond", serif; font-weight: 500; font-size: 32px; color: var(--ink); letter-spacing: 1px;
  }
  .phone-band {
    position: absolute; left: 338px; width: 525px; top: 667px; height: 44px;
    background: var(--purple); color: #fff; text-align: center;
    font-family: "Cormorant Garamond", serif; font-weight: 500; font-size: 36px; line-height: 44px; letter-spacing: 4px;
    font-variant-numeric: lining-nums;
  }
  .email, .web {
    position: absolute; left: 338px; width: 525px; text-align: center; color: var(--ink);
    font-family: "Cormorant Garamond", serif; font-weight: 500; text-transform: uppercase;
  }
  .email { top: 721px; font-size: 14px; letter-spacing: 1px; }
  .web { top: 761px; font-size: 16px; letter-spacing: 1px; }
</style>
</head>
<body>
  <section class="card card--front" aria-label="Card front"></section>
  <div class="brand-name">Ashcombe &amp; Vale</div>
  <div class="brand-rule" aria-hidden="true"></div>

  <ul class="services services--a"><li>Weddings</li><li>Birthdays</li></ul>
  <ul class="services services--b"><li>Conferences</li><li>Product Launches</li></ul>
  <ul class="services services--c"><li>Fashion Shows</li><li>Conventions</li></ul>

  <svg class="divider divider--front" viewBox="0 0 375 10" aria-hidden="true">
    <line x1="0" y1="5" x2="375" y2="5" stroke="#555" stroke-width="1"/>
    <rect x="183" y="1.5" width="7" height="7" transform="rotate(45 186.5 5)" fill="#fff" stroke="#555"/>
  </svg>

  <div class="areas-label">IN THE FOLLOWING AREAS</div>
  <div class="areas">Wiltshire / Oxfordshire / Berkshire / London</div>

  <section class="card card--back" aria-label="Card back"></section>
  <div class="flourish" role="img" aria-label="Decorative scroll ornament above a fine rule"></div>
  <div class="person">MOIRA LINTELL</div>
  <div class="phone-band">07741 308562</div>
  <div class="email">moira@amberfinchgatherings.co.uk</div>
  <svg class="divider divider--back" viewBox="0 0 375 10" aria-hidden="true">
    <line x1="0" y1="5" x2="375" y2="5" stroke="#555" stroke-width="1"/>
    <rect x="183" y="1.5" width="7" height="7" transform="rotate(45 186.5 5)" fill="#fff" stroke="#555"/>
  </svg>
  <div class="web">www.amberfinchgatherings.co.uk</div>
</body>
</html>
```